KFR T Coaching Website

We need a website to post videos, blogs and other information or links.
We teach Jujitsu , combatives, Metaphysical Coaching. I want to tach online and in person. Silver Harbor Institute Deals in several areas of Personal Protection and Coaching.
Training (Martial Arts / combative)
Emotional Intelligence
Leadership Development
Motivation
Our Log is attached.
Similar Websites to what we do ( we want to stand out better).
https://renwoskel.com/
https://bavomure.com/
https://crestlinevigorcoaching.com/
Training , Martial Arts, coaching
2 page

```html
<!DOCTYPE html>
<html lang="en">
<head>
<meta charset="utf-8">
<title>Silver Harbor Institute — Martial Arts &amp; Coaching</title>
<link rel="stylesheet" href="https://fonts.googleapis.com/css2?family=Italiana&family=Montserrat:ital,wght@0,400;0,500;0,600;0,700;1,400&display=swap">
<style>
:root{
  --red:#e3141c;
  --ink:#141414;
  --dark:#181818;
  --paper:#ffffff;
  --mist:#f2eeee;
  --grey:#8a8a8a;
  --line:#e6e6e6;
  --display:'Italiana', serif;
  --sans:'Montserrat', sans-serif;
}
*{box-sizing:border-box;margin:0;padding:0}
html,body{width:1200px;height:4955px;overflow:hidden}
body{position:relative;background:var(--paper);font-family:var(--sans);color:var(--ink)}
.abs{position:absolute}
.btn{display:inline-flex;align-items:center;justify-content:center;background:var(--red);color:#fff;font:600 11px var(--sans);text-decoration:none}
.btn-outline{background:transparent;border:2px solid var(--red);color:var(--red)}
.photo{display:block}
.display{font-family:var(--display);font-weight:400;letter-spacing:1px}

/* nav */
.nav{top:0;left:0;width:1200px;height:54px;background:#fff;z-index:5}
.nav a{position:absolute;top:20px;font:500 11px var(--sans);color:var(--ink);text-decoration:none}
.nav .btn{top:10px;left:889px;width:105px;height:34px;font-size:11px}
.brand{position:absolute;left:513px;top:0;width:174px;height:128px;background:#fff;border-bottom-left-radius:87px 60px;border-bottom-right-radius:87px 60px;border-bottom:3px solid var(--red);display:flex;flex-direction:column;align-items:center;justify-content:center;padding-top:10px;gap:8px}
.brand-dot{width:26px;height:26px;border-radius:50%;background:var(--red)}
.brand-name{font:700 10px var(--sans);color:var(--ink);letter-spacing:.5px;text-align:center;text-transform:uppercase;line-height:1.3}

/* hero */
.hero{top:54px;left:0;width:1200px;height:596px;background:radial-gradient(ellipse at 55% 40%,#5b4634 0%,#2a211b 45%,#120e0c 100%)}
.hero h1{position:absolute;top:200px;left:0;width:1200px;text-align:center;color:#fff;font-size:62px;line-height:56px}
.hero .btn{position:absolute;top:339px;left:543px;width:114px;height:34px}

/* services */
.section-title{font-size:58px;color:var(--ink)}
.services-title{top:735px;left:205px}
.services-all{top:751px;left:895px;width:98px;height:34px}
.card{width:266px;height:320px;background:var(--ink)}
.card .photo{width:266px;height:222px}
.card h3{position:absolute;left:38px;top:242px;color:#fff;font:700 14px var(--sans);letter-spacing:.3px}
.card .more{position:absolute;left:38px;top:292px;color:#ccc;font:600 7px var(--sans);letter-spacing:.6px}
.card svg{position:absolute;right:34px;top:287px}
.card .rule{position:absolute;left:38px;right:34px;top:275px;height:1px;background:#3a3a3a}

/* about */
.about{top:1654px;left:0;width:1200px;height:553px;background:var(--dark);overflow:hidden}
.about-side{position:absolute;left:0;top:0;width:320px;height:553px;background:var(--mist)}
.about-word{position:absolute;left:30px;top:0;height:553px;writing-mode:vertical-rl;transform:rotate(180deg);font:400 104px/104px var(--display);color:#d9d0d0;letter-spacing:4px;white-space:nowrap;text-align:center}
.about-photo{position:absolute;left:270px;top:0;width:290px;height:553px;background:linear-gradient(180deg,#e9e5e0 0%,#d9d4ce 55%,#c6c1bb 100%)}
.about h2{position:absolute;left:702px;top:86px;color:#fff;font-size:46px;line-height:50px}
.about p{position:absolute;left:702px;top:217px;width:330px;color:#ddd;font:400 10.5px/20px var(--sans)}
.about .btn{position:absolute;left:803px;top:423px;width:98px;height:34px;font-size:7px}

/* posts */
.posts-title{top:2285px;left:0;width:1200px;text-align:center}
.explore{top:2450px;left:121px;font:600 18px/25px var(--sans)}
.cat{width:198px;height:137px;display:flex;align-items:center;justify-content:center}
.cat span{border:1px solid #fff;color:#fff;font:500 14px var(--sans);letter-spacing:1px;padding:3px 14px;background:rgba(255,255,255,.25)}
.grid{top:2650px;left:76px;width:1048px;display:flex}
.col{width:262px;padding:0 16px;border-right:1px solid var(--line);display:flex;flex-direction:column}
.col:last-child{border-right:none}
.post{padding:0 0 30px}
.post + .post{border-top:1px solid var(--line);margin:0 -16px;padding:30px 16px}
.post .photo{width:225px;margin-bottom:20px}
.tag{font:700 8px var(--sans);letter-spacing:.5px;margin-bottom:8px}
.post h4{font:600 14px/19px var(--sans);margin-bottom:14px}
.post h4.red{color:#8c1a1a}
.post p{font:400 9.5px/15px var(--sans);color:var(--grey)}
.quote-mark{font:700 30px var(--display);color:var(--ink);line-height:24px;margin:6px 0 4px}
.play{position:relative}
.play i{position:absolute;left:50%;top:50%;width:30px;height:30px;margin:-15px 0 0 -15px;border-radius:50%;background:#fff}
.play i::after{content:"";position:absolute;left:12px;top:9px;border-left:9px solid var(--red);border-top:6px solid transparent;border-bottom:6px solid transparent}
.load{top:3558px;left:546px;width:111px;height:35px;font-size:7px}

/* testimonials */
.testi{top:3688px;left:0;width:1200px;height:552px;background:var(--dark);overflow:hidden}
.testi-side{position:absolute;left:808px;top:0;width:392px;height:552px;background:var(--mist)}
.testi-word{position:absolute;left:1092px;top:0;height:520px;writing-mode:vertical-rl;transform:rotate(180deg);font:400 92px/92px var(--display);color:#d3caca;letter-spacing:3px;white-space:nowrap;text-align:left}
.testi-photo{position:absolute;left:606px;top:112px;width:300px;height:300px;border-radius:50%;background:radial-gradient(circle at 50% 50%,#d4cfcf 0%,#e6e2e2 70%,#efecec 100%)}
.testi h2{position:absolute;left:205px;top:115px;color:#fff;font-size:46px}
.testi blockquote{position:absolute;left:205px;top:210px;width:300px;color:#bdbdbd;font:italic 400 16px/28px var(--sans)}
.testi .who{position:absolute;left:205px;top:402px;color:#fff;font:700 15px var(--sans)}
.testi .role{position:absolute;left:216px;top:422px;color:#aaa;font:400 9px var(--sans)}
.arrows{position:absolute;left:37px;top:518px;display:flex;gap:16px}

/* cta */
.cta{top:4240px;left:0;width:1200px;height:327px;background:radial-gradient(ellipse at 50% 50%,#4a0a0c 0%,#8f0d12 45%,#d01219 75%,#3a0608 100%)}
.cta h2{position:absolute;top:62px;left:0;width:1200px;text-align:center;color:#fff;font-size:60px;line-height:64px}
.cta .btn{position:absolute;top:232px;left:551px;width:98px;height:38px;background:#fff;color:var(--red);font-size:8px}

/* footer */
.foot h5{font:600 11px var(--sans);color:var(--ink);margin-bottom:28px}
.foot h5.muted{color:#b0b0b0;font-weight:500}
.foot li{list-style:none;font:500 9px/25px var(--sans)}
.foot p{font:400 8px/15px var(--sans);color:#555}
.sub{top:4655px;left:205px;width:220px}
.sub-form{margin-top:24px;display:flex}
.sub-form span{width:160px;height:32px;background:#f1f1f1;font:600 7px var(--sans);display:flex;align-items:center;padding-left:18px}
.sub-form b{width:36px;height:32px;background:var(--red);display:flex;align-items:center;justify-content:center}
.fnav{top:4655px;left:525px}
.hours{top:4655px;left:679px}
.contact{top:4655px;left:853px;width:160px}
.contact .lbl{font:400 7px var(--sans);color:#aaa;margin-top:10px}
.contact .val{font:600 9px/15px var(--sans);color:var(--ink)}
.contact a{color:var(--red);font:600 9px var(--sans)}
.foot-rule{top:4897px;left:205px;width:790px;height:1px;background:var(--line)}
.copy{top:4916px;left:205px;font:400 8px var(--sans);color:#777}
.copy b{color:var(--ink)}
.social{top:4910px;left:870px;display:flex;gap:26px}
.social i{width:10px;height:10px;border-radius:50%;background:#444;display:block}
</style>
</head>
<body>

<header class="abs nav">
  <a style="left:205px" href="#">About Us</a>
  <a style="left:283px" href="#">Training</a>
  <a style="left:356px" href="#">Latest Blog</a>
  <div class="brand"><span class="brand-dot"></span><span class="brand-name">Silver Harbor<br>Institute</span></div>
  <a style="left:748px" href="#">Video</a>
  <a style="left:810px" href="#">Contact</a>
  <a class="btn" href="#">Book a Demo</a>
</header>

<section class="abs hero" role="img" aria-label="Two martial artists in gi grappling on a dojo mat in warm low light">
  <h1 class="display">Start your training<br>in Martial Arts</h1>
  <a class="btn" href="#">Our Services</a>
</section>

<h2 class="abs section-title display services-title">Our Services</h2>
<a class="abs btn services-all" href="#">View All</a>

<article class="abs card" style="left:169px;top:865px"><div class="photo" style="background:linear-gradient(135deg,#3c3c3c,#9b9b9b 50%,#222)" role="img" aria-label="Instructor demonstrating a defensive hold"></div><h3>Personal Protection</h3><span class="rule"></span><span class="more">LEARN MORE</span><svg width="18" height="10" viewBox="0 0 18 10"><path d="M0 5h16M12 1l4 4-4 4" stroke="#fff" fill="none" stroke-width="1.2"/></svg></article>
<article class="abs card" style="left:467px;top:865px"><div class="photo" style="background:linear-gradient(180deg,#d8d8d8,#a9a9a9)" role="img" aria-label="Coach guiding a student on a grappling mat"></div><h3>Coaching</h3><span class="rule"></span><span class="more">LEARN MORE</span><svg width="18" height="10" viewBox="0 0 18 10"><path d="M0 5h16M12 1l4 4-4 4" stroke="#fff" fill="none" stroke-width="1.2"/></svg></article>
<article class="abs card" style="left:765px;top:865px"><div class="photo" style="background:linear-gradient(135deg,#cfd6e0,#d79b8a 55%,#5f7fb0)" role="img" aria-label="Students practising punches in a class"></div><h3>Training</h3><span class="rule"></span><span class="more">LEARN MORE</span><svg width="18" height="10" viewBox="0 0 18 10"><path d="M0 5h16M12 1l4 4-4 4" stroke="#fff" fill="none" stroke-width="1.2"/></svg></article>
<article class="abs card" style="left:169px;top:1219px"><div class="photo" style="background:linear-gradient(135deg,#e9e4df,#b9a58f 60%,#6b5a4b)" role="img" aria-label="Counsellor speaking with a stressed client"></div><h3>Emotional Intelligence</h3><span class="rule"></span><span class="more">LEARN MORE</span><svg width="18" height="10" viewBox="0 0 18 10"><path d="M0 5h16M12 1l4 4-4 4" stroke="#fff" fill="none" stroke-width="1.2"/></svg></article>
<article class="abs card" style="left:467px;top:1219px"><div class="photo" style="background:linear-gradient(135deg,#3a3a3a,#8e7e74 50%,#262626)" role="img" aria-label="Group of students during a partner drill"></div><h3>Leadership Development</h3><span class="rule"></span><span class="more">LEARN MORE</span><svg width="18" height="10" viewBox="0 0 18 10"><path d="M0 5h16M12 1l4 4-4 4" stroke="#fff" fill="none" stroke-width="1.2"/></svg></article>
<article class="abs card" style="left:765px;top:1219px"><div class="photo" style="background:linear-gradient(180deg,#7fb2d8,#2a4f9e 70%,#1d2f6b)" role="img" aria-label="Fighter in blue gi in a ready stance"></div><h3>Motivation</h3><span class="rule"></span><span class="more">LEARN MORE</span><svg width="18" height="10" viewBox="0 0 18 10"><path d="M0 5h16M12 1l4 4-4 4" stroke="#fff" fill="none" stroke-width="1.2"/></svg></article>

<section class="abs about">
  <div class="about-side"></div>
  <div class="about-word">COACHING</div>
  <div class="about-photo" role="img" aria-label="Photo of the head instructor in a white gi"></div>
  <h2 class="display">About Silver<br>Harbor Institute</h2>
  <p>Lorem ipsum dolor sit amet, consectetur adipiscing elit, sed do eiusmod tempor incididunt ut labore et dolore magna aliqua. Quis ipsum suspendisse ultrices gravida. Risus co mmodo viverra maecenas accumsan lacus vel facilisis. Lorem ipsum dolor sit amet, consectetur adipiscing elit. Quisque condimentum laoreet imperdiet. Mauris velit metus, sagittis at nibh a, posuere suscipit enim. Pellentesque sollicitudin, sapien a fringilla porttitor, elit enim eleifend risus, sit amet eleifend. fringil elit velite .</p>
  <a class="btn btn-outline" href="#">READ MORE</a>
</section>

<h2 class="abs section-title display posts-title">Latest Posts</h2>
<div class="abs explore">Explore Our<br>General<br>Categories</div>
<a class="abs cat" style="left:281px;top:2421px;background:linear-gradient(135deg,#d9d3cb,#8a7c6c)" role="img" aria-label="Laptop on a desk"><span>BLOGS</span></a>
<a class="abs cat" style="left:490px;top:2421px;background:linear-gradient(135deg,#f0c890,#a55a20 55%,#3a1e10)" role="img" aria-label="Video camera in warm light"><span>VIDEOS</span></a>
<a class="abs cat" style="left:700px;top:2421px;background:linear-gradient(135deg,#9aa3ad,#3c4550)" role="img" aria-label="Newsroom desk with monitors"><span>NEWS</span></a>
<a class="abs cat" style="left:910px;top:2421px;background:linear-gradient(135deg,#6a6a6a,#e5e5e5 50%,#2a2a2a)" role="img" aria-label="Martial artist in a white gi"><span>QUOTE</span></a>

<div class="abs grid">
  <div class="col">
    <div class="post"><div class="photo" style="height:150px;background:linear-gradient(135deg,#ddd,#555 55%,#a33)" role="img" aria-label="Two fighters sparring"></div><div class="tag">NEWS</div><h4 class="red">Lorem ipsum dolor sit amet consectetur adipiscing.</h4><p>Consectetur adipiscing elit, sed do eiusm od tempor incididunt ut labore et dolore magna aliqua. Ut enim ad minim veniam quis nostrud exercitation ullamco laboris nisi ut aliquip ex ea commodo consequat duis aute irure dolor in reprehenderit.</p></div>
    <div class="post"><div class="tag">NEWS</div><h4>Etiam rhoncus quis mauris quis hendrerit</h4><p>As we work to take this magazine and community to the next level, our strategist Nora Fenwick wanted to reflect on where this project came from. So she sat down to chat with our founder and editor in chief Ellis Marrow. Here's the result!</p></div>
    <div class="post"><div class="tag">BLOGS</div><h4>augue finibus porttitor</h4><p>Ut enim ad minim veniam, quis nostrud exercitation ullamco laboris nisi ut aliquip ex ea commodo consequat. Duis aute ir ure dolor in reprehenderit.</p></div>
  </div>
  <div class="col">
    <div class="post"><div class="photo play" style="height:215px;background:linear-gradient(180deg,#e2e2e2,#9a9a9a)" role="img" aria-label="Coach teaching a ground technique"><i></i></div><div class="tag">VIDEOS</div><h4>Proin semper a ligula et scelerisque. Quisque tincidunt elementum</h4><p>Whether it's the 2020 Regional Debate League champion, three 2021 national finalists, or three 2022 league middleschool finalists (including the national champion), Brightpath has a history of excellence in cultivating standout orators. While many of our coaches were oratory champs in their day, we refuse to write students' speeches.</p></div>
    <div class="post"><div class="photo play" style="height:130px;background:linear-gradient(180deg,#8dc0e6,#2c56a6)" role="img" aria-label="Fighter in blue gi"><i></i></div><div class="tag">VIDEOS</div><h4>empor ante vel, consequat</h4><p>Cetetur adipiscing elit, sed do eiusmod tempor incididunt ut labore et dolore magna aliqua. Ut enim ad minim veniam quis nostrud exercitation ullamco laboris nisi ut aliquip ex ea commodo</p></div>
  </div>
  <div class="col">
    <div class="post"><div class="photo play" style="height:180px;background:linear-gradient(135deg,#4a4a4a,#b3b3b3 50%,#222)" role="img" aria-label="Close grappling exchange"><i></i></div><div class="tag">VIDEOS</div><h4>Praesent a sapien at nisl sodales ornare</h4><p>Quis nostrud exercitation ullamco laboris nisi ut aliquip ex ea commodo consequat uis aute irure dolor in reprehenderit in voluptate velit esse cillum dolore.</p></div>
    <div class="post"><div class="photo" style="height:130px;background:linear-gradient(135deg,#3a3a3a,#9c8c80 55%,#2a2a2a)" role="img" aria-label="Students in a group drill"></div><div class="tag">NEWS</div><h4>arcu posuere consectetur</h4><p>Adipiscing elit, sed do eiusmod tempor incididunt ut labore et dolore</p></div>
    <div class="post"><div class="tag">BLOGS</div><h4>Quisque tincidunt elemen</h4><p>Exercitation ullamco laboris nisi ut aliqu ip ex ea commodo consequat. Duis aute irure dolor in reprehenderit in voluptate velit esse cillum dolore eu.</p></div>
  </div>
  <div class="col">
    <div class="post"><div class="tag">QUOTE</div><div class="quote-mark">“</div><p>"Lorem ipsum dolor sit amet, consectetur adipiscing elit, sed do eiusd tempor incididunt ut labore et dolore magna aliqua. Ut enim ad minim veniam quis nostrud excitation."</p></div>
    <div class="post"><div class="photo" style="height:150px;background:linear-gradient(135deg,#cfd6e0,#d79b8a 55%,#5f7fb0)" role="img" aria-label="Class practising strikes"></div><div class="tag">NEWS</div><h4>vestibulum porttitor dapibus. Aliquam sit amet purus ac augue finibus porttitor</h4><p>Tempor incididunt ut labore et dolore magna aliqua. Ut enim ad minim veniam, quis nostrud exercitation</p><p style="margin-top:10px">Elit, sed do eiusmod tempor incididunt ut labore et dolore magna aliqua. Ute nim ad minim veniam, quis nostrud ore ipsum dolor sit amet, consectetur adipiscing elit.</p></div>
    <div class="post"><div class="tag">BLOGS</div><h4>ulputate accumsan</h4><p>Exercitation ullamco laboris nisi ut aliquip ex ea commodo consequat. Duis aute irure dolor in reprehenderit in voluptate velit esse cillum dolore eu fugiat nulla pa riatur excepteur.</p></div>
  </div>
</div>
<a class="abs btn btn-outline load" href="#">LOAD MORE</a>

<section class="abs testi">
  <div class="testi-side"></div>
  <div class="testi-word">TESTIMONIALS</div>
  <div class="testi-photo" role="img" aria-label="Round portrait of a student in a black gi"></div>
  <h2 class="display">Testimonials</h2>
  <blockquote>"Dolor sit amet, consecteturadipis cingelit Vestibulum ac gravida est Lorem ipsum dolor sit ame cons ectetur adipi scing elit. Ve bulum ac gravida est.Morbi tristique met us non leo sollicitudin"</blockquote>
  <div class="who">- Marcus Vale</div>
  <div class="role">Donec sem mi semper</div>
  <div class="arrows">
    <svg width="26" height="12" viewBox="0 0 26 12"><path d="M26 6H2M7 1L2 6l5 5" stroke="#fff" fill="none" stroke-width="1.4"/></svg>
    <svg width="26" height="12" viewBox="0 0 26 12"><path d="M0 6h24M19 1l5 5-5 5" stroke="#fff" fill="none" stroke-width="1.4"/></svg>
  </div>
</section>

<section class="abs cta" role="img" aria-label="Red-toned close-up of a fighter in motion">
  <h2 class="display">Pain is weakness<br>leaving the body</h2>
  <a class="btn" href="#">Join Us</a>
</section>

<footer class="foot">
  <div class="abs sub"><h5>Subscribe Our Newsletter</h5><p>Lorem ipsum dolor sit amet, consectetur adipi elit, sed do eiusmod tempor.</p>
    <div class="sub-form"><span>Enter your email...</span><b><svg width="14" height="12" viewBox="0 0 14 12"><path d="M0 6L14 0 10 12 7 7z" fill="#fff"/></svg></b></div></div>
  <div class="abs fnav"><h5 class="muted">Navigation</h5><ul><li>Home</li><li>About Us</li><li>Training</li><li>Blog</li><li>Video</li><li>Contact</li></ul></div>
  <div class="abs hours"><h5 class="muted">Opening Hours</h5><ul><li>Monday 8AM-5PM</li><li>Tuesday 8AM-5PM</li><li>Wednesday 8AM-5PM</li><li>Thursday 8AM-5PM</li><li>Friday 8AM-5PM</li></ul></div>
  <div class="abs contact"><h5 class="muted" style="margin-bottom:18px">Contact</h5>
    <div class="lbl">Address:</div><div class="val">Address line comes here,<br>Lorem ipsum 123456</div>
    <div class="lbl">Phone:</div><div class="val" style="font-size:12px">0123 456 7890</div>
    <div class="lbl">Email:</div><a href="#">hello@silverharbor-inst.com</a></div>
  <div class="abs foot-rule"></div>
  <div class="abs copy">© 2022 <b>Silver Harbor Institute.</b> All Right Reserved.</div>
  <div class="abs social"><i></i><i></i><i></i><i></i></div>
</footer>

</body>
</html>
```